Polling website project

We need a website design for a polling website called vextiq.com. This will be a website where visitors can take and create polls for various topics along with view results. We want something really simple and "web 2.0." We are going to make a cell phone app that goes along with the website and we want the look and feel of the website to be very "app-like." Basically that means minimalistic design with a poll being the center of the page.
When someone comes to the site, we want them to see basically just a poll in the center of the screen and a toolbar at the top of the page with links to login fields/user profile, post a new poll, view friends list, a drop-down list of poll topics, and a search bar. We need about three pages mocked up: a home page/poll view page, a user control panel/profile page, a submit new poll page.
We also want our logo/header to have a "pulse" theme. The name vextiq is supposed to be a play on the word pulse, we'd like the logo to make that obvious, maybe the use of the EKG graph could work.
We also want a nice tab in the corner to sign up that is attractive and flashy, kind of like the feedback tab on the side of this website.
Target Market(s)
Teens and young adults, the chatterloop crowd
Industry/Entity Type
Cell Phone
Look and feel
Each slider illustrates characteristics of the customer's brand and the style your logo design should communicate.

```html
<!DOCTYPE html>
<html lang="en">
<head>
<meta charset="utf-8">
<title>vextiq – Create Your Own Poll Free</title>
<link rel="stylesheet" href="https://fonts.googleapis.com/css2?family=Open+Sans:wght@400;600;700&display=swap">
<style>
:root{
  --header:#2a2e33;
  --header-line:#3a3f45;
  --hero-top:#1f86d3;
  --hero-bottom:#6fc0ef;
  --panel:#1c7fd0;
  --panel-edge:#0f66b0;
  --card:#f3f8fc;
  --ink:#333;
  --muted:#6b6b6b;
  --link:#1a84c8;
  --accent:#2a9be6;
  --footer:#ececec;
  --footer-bar:#dcdcdc;
  --page:#ffffff;
}
*{box-sizing:border-box;margin:0;padding:0}
html,body{width:857px;height:1200px;overflow:hidden}
body{background:var(--page);font-family:"Open Sans",Arial,sans-serif;color:var(--ink);position:relative;font-size:9px;line-height:1.45}
a{color:var(--link);text-decoration:none}

.site-header{position:absolute;left:0;top:0;width:857px;height:46px;background:var(--header);border-bottom:1px solid var(--header-line)}
.brand{position:absolute;left:30px;top:6px;display:flex;align-items:center;gap:7px}
.brand-dot{width:10px;height:10px;border-radius:50%;background:var(--accent)}
.brand-name{color:#fff;font-size:22px;font-weight:700;line-height:1}
.brand-tagline{position:absolute;left:47px;top:31px;color:#9fb3c4;font-size:7px;letter-spacing:.3px}
.main-nav{position:absolute;right:26px;top:13px;display:flex;gap:6px}
.main-nav a{color:#e6e6e6;font-size:10px;padding:4px 14px;border-radius:3px}
.main-nav a.active{background:#fff;color:var(--ink);font-weight:600}

.hero{position:absolute;left:0;top:46px;width:857px;height:365px;background:linear-gradient(180deg,var(--hero-top),var(--hero-bottom))}
.poll-panel{position:absolute;left:28px;top:100px;width:800px;height:212px;background:var(--panel);border:1px solid var(--panel-edge);border-radius:6px;box-shadow:0 2px 6px rgba(0,0,0,.25)}
.poll-panel h1{position:absolute;left:22px;top:12px;color:#fff;font-size:19px;font-weight:600}
.poll-inner{position:absolute;left:12px;top:52px;width:776px;height:146px;background:var(--card);border-radius:4px}
.quick-poll{position:absolute;left:14px;top:14px;width:350px;height:118px;border:1px solid #cfe0ee;border-radius:4px;background:#fff;padding:10px 14px}
.quick-poll p{color:var(--link);font-size:10px;font-weight:600;width:240px}
.option{display:flex;align-items:center;gap:6px;margin-top:6px;font-size:9px;color:var(--ink)}
.radio{width:9px;height:9px;border-radius:50%;border:1px solid #8aa;background:#fff}
.vote-btn{position:absolute;left:14px;bottom:10px;background:var(--link);color:#fff;font-size:8px;font-weight:700;padding:3px 12px;border-radius:3px}
.setup-form{position:absolute;left:392px;top:14px;width:370px;height:118px;border:1px solid #cfe0ee;border-radius:4px;background:#fff;padding:10px 14px}
.setup-form label{display:block;font-size:9px;color:var(--ink);margin-bottom:5px}
.field{height:16px;border:1px solid #c9d6e0;border-radius:2px;margin-bottom:5px;padding:2px 6px;font-size:8px;color:#888;background:#fafcfd}
.form-row{display:flex;gap:8px}
.form-row .field{flex:1}
.start-btn{background:var(--accent);color:#fff;font-size:11px;font-weight:600;padding:2px 16px;border-radius:3px;height:18px}

.features{position:absolute;left:43px;top:423px;width:785px;display:flex;gap:28px}
.feature{width:243px}
.feature-image{height:105px;border-radius:2px}
.feature h2{font-size:15px;font-weight:600;margin:12px 0 6px}
.feature p{color:var(--muted);font-size:8px}
.read-more{display:inline-block;margin-top:6px;font-size:9px;font-weight:600}

.divider{position:absolute;left:28px;top:690px;width:800px;height:1px;background:#ddd}

.info{position:absolute;left:43px;top:706px;width:785px;display:flex;gap:28px}
.info-col{width:243px}
.info-col h3{font-size:14px;font-weight:600;margin-bottom:8px}
.item-title{color:var(--link);font-size:9px;font-weight:600}
.info-col p{color:var(--muted);font-size:8px;margin-bottom:8px}
.blog-post{display:flex;gap:8px;margin-bottom:10px}
.blog-thumb{width:52px;height:48px;flex:none}
.testimonial{margin-bottom:10px}
.testimonial .headline{color:var(--link);font-size:10px;font-weight:600}
.author{display:block;text-align:right;color:var(--link);font-size:8px;font-weight:700;font-style:italic;text-transform:uppercase}

.site-footer{position:absolute;left:0;top:985px;width:857px;height:175px;background:var(--footer);border-top:1px solid #ddd}
.footer-cols{position:absolute;left:43px;top:18px;display:flex;gap:42px}
.footer-col h4{font-size:10px;font-weight:600;margin-bottom:6px}
.footer-col li{list-style:none;font-size:8px;color:var(--muted);line-height:1.6}
.social{display:flex;gap:5px;margin-bottom:6px}
.social span{width:16px;height:16px;border-radius:3px;background:#9aa6b0}
.social-links{font-size:8px;color:var(--muted)}
.footer-bar{position:absolute;left:0;top:1160px;width:857px;height:40px;background:var(--footer-bar);padding:14px 43px;font-size:8px;color:var(--muted)}
</style>
</head>
<body>

<header class="site-header">
  <div class="brand"><span class="brand-dot"></span><span class="brand-name">vextiq</span></div>
  <div class="brand-tagline">Every Voice Counts Here</div>
  <nav class="main-nav">
    <a class="active" href="#">Home</a><a href="#">About Us</a><a href="#">Services</a><a href="#">Treatment</a><a href="#">Blog</a><a href="#">Contact</a>
  </nav>
</header>

<section class="hero">
  <div class="poll-panel">
    <h1>Now! Create Your on Poll Free</h1>
    <div class="poll-inner">
      <div class="quick-poll">
        <p>Would you like to setup polls on your Website ?</p>
        <div class="option"><span class="radio"></span>Yes</div>
        <div class="option"><span class="radio"></span>No</div>
        <span class="vote-btn">VOTE</span>
      </div>
      <div class="setup-form">
        <label>Would you like a setup polls on your website?</label>
        <div class="field">Yes</div>
        <div class="field">No</div>
        <div class="form-row"><div class="field">your email address</div><span class="start-btn">Start Polling !</span></div>
      </div>
    </div>
  </div>
</section>

<section class="features">
  <article class="feature">
    <div class="feature-image" role="img" aria-label="Photo of a smiling person creating a poll on a laptop" style="background:linear-gradient(135deg,#e8e4dc,#b9c2c8)"></div>
    <h2>Crete Poll Now</h2>
    <p>Build a fresh poll in seconds with our simple editor. Pick a topic, add your answers, choose colours and share the link with friends so everyone can vote from their phone or the web straight away.</p>
    <a class="read-more" href="#">read more ›</a>
  </article>
  <article class="feature">
    <div class="feature-image" role="img" aria-label="Photo of a hand pointing at a rising chart" style="background:linear-gradient(135deg,#f4f4f4,#c9d3da)"></div>
    <h2>Publish Now</h2>
    <p>Publish your poll to your profile, your friends list or the public topic feed. Embed it on any website with one short line, and watch the votes arrive live as people everywhere join the conversation today.</p>
    <a class="read-more" href="#">read more ›</a>
  </article>
  <article class="feature">
    <div class="feature-image" role="img" aria-label="Colourful 3D pie chart and bar chart illustration" style="background:linear-gradient(135deg,#f2c14a,#3fa0d8 55%,#7cc35a)"></div>
    <h2>Analyze Result</h2>
    <p>See clear results the moment votes come in. Charts update live, filters show how each group answered, and you can export the numbers or share a results card with your followers whenever the poll closes.</p>
    <a class="read-more" href="#">read more ›</a>
  </article>
</section>

<div class="divider"></div>

<section class="info">
  <div class="info-col">
    <h3>Why Choose us?</h3>
    <div class="item-title">Title Line here</div>
    <p>Our polls load fast on every phone, look clean on any screen and take only a few taps to answer. Teens and young adults use them every day to settle debates, pick plans and hear what their friends really think about anything.</p>
    <p>Everything is free to start. Create unlimited polls, follow trending topics, invite friends and keep your results private or public. Our team keeps adding new features based on what the community asks for most.</p>
    <a class="read-more" href="#">read more ›</a>
  </div>
  <div class="info-col">
    <h3>Recent Blog Post</h3>
    <div class="blog-post">
      <div class="blog-thumb" role="img" aria-label="Blog thumbnail photo" style="background:linear-gradient(135deg,#c9a27a,#6b8fa8)"></div>
      <div><div class="item-title">Title line here</div><p>Five quick tips for writing poll questions that people actually want to answer and share.</p></div>
    </div>
    <div class="blog-post">
      <div class="blog-thumb" role="img" aria-label="Blog thumbnail photo" style="background:linear-gradient(135deg,#9bb7cf,#3d6f9a)"></div>
      <div><div class="item-title">Title line here</div><p>How our mobile app keeps your polls in sync with the website wherever you go.</p></div>
    </div>
    <div class="blog-post">
      <div class="blog-thumb" role="img" aria-label="Blog thumbnail photo" style="background:linear-gradient(135deg,#d8c7a6,#8a7256)"></div>
      <div><div class="item-title">Title line here</div><p>This week's most popular topics and the surprising results our community voted for.</p></div>
    </div>
  </div>
  <div class="info-col">
    <h3>Testimonials</h3>
    <div class="testimonial">
      <div class="headline">Headline goes here</div>
      <p>I made a poll for my class trip and everyone voted within an hour. It is so easy to use and the results page looks great on my phone.</p>
      <span class="author">By Author Name</span>
    </div>
    <div class="testimonial">
      <div class="headline">Headline goes here</div>
      <p>We use it every week to pick our team name, music and food. Sharing a poll with friends takes seconds and the live charts make it really fun.</p>
      <span class="author">By Author Name</span>
    </div>
  </div>
</section>

<footer class="site-footer">
  <div class="footer-cols">
    <div class="footer-col"><h4>vextiq</h4><ul><li>Home page</li><li>Return Blog</li><li>Services Overview</li><li>Featured</li><li>Why We Are</li></ul></div>
    <div class="footer-col"><h4>About Us</h4><ul><li>Our Company</li><li>How We Work</li><li>Testimonials</li></ul></div>
    <div class="footer-col"><h4>Services</h4><ul><li>Projects</li><li>Success Stories</li><li>Support</li></ul></div>
    <div class="footer-col"><h4>Support &amp; FAQ</h4><ul><li>Partners</li><li>Member Login</li><li>FAQ</li><li>Stay Connected</li></ul></div>
    <div class="footer-col"><h4>Stay In Touch</h4>
      <div class="social"><span></span><span></span><span></span></div>
      <div class="social-links">chatterloop | Chirpnest | Linkfold</div>
    </div>
  </div>
</footer>
<div class="footer-bar">© 2012 Company Name | All right reserved.</div>

</body>
</html>
```